PVQ BOOK COVER 6 X 9 - MARKET LEADING LEADERSHIP BOOK

I need a book cover designed for a book called Steering Through the Era of Circuits – Enduring Insight for an Automated Century and some more stuff, which you can see in the image I generated. I created a basic cover, but it needs to wow; it's about leadership, ancient wisdom, and AI. This book offers a unique approach: combining 2,000-year-old Stoic philosophy with practical frameworks for modern AI-age leadership challenges. Rather than another technical book about AI, this is a deeply human guide for leaders who want to harness AI's power while preserving their organisation's humanity.

Target Market(s)

EXECUTIVES, LEADERS MANAGERS DEALING WITH AI

Industry/Entity Type

LEADERSHIP

Requirements
Must have
• MUSIC BE CLASSY AND A SOLID COMBINATION OF ANCIENT WISDOM AND FUTURISTIC AI
Nice to have
• GIVE ME THE BEST YOU HAVE
Should not have
• NON

```html
<!DOCTYPE html>
<html lang="en">
<head>
<meta charset="utf-8">
<title>Steering Through the Era of Circuits – Book Cover</title>
<link rel="stylesheet" href="https://fonts.googleapis.com/css2?family=Montserrat:wght@800&family=Open+Sans:wght@700&family=Bebas+Neue&display=swap">
<style>
  :root {
    --backdrop: #8f8f8f;
    --paper: #ffffff;
    --ink: #050505;
    --blue-deep: #0b6fb3;
    --blue-bright: #0fbee6;
    --photo-dark: #141433;
    --photo-mid: #3a2a5e;
    --photo-glow: #ff9a3c;
    --white: #ffffff;
  }
  * { margin: 0; padding: 0; box-sizing: border-box; }
  html, body {
    width: 1200px; height: 1200px; overflow: hidden;
    background: var(--backdrop);
  }
  .cover {
    position: absolute; left: 260px; top: 91px;
    width: 679px; height: 1018px;
    background: var(--paper);
    overflow: hidden;
  }
  .title-art {
    position: absolute; left: 0; top: 0;
    width: 679px; height: 560px;
  }
  .title-line { font-family: "Montserrat", sans-serif; font-weight: 800; }
  .subtitle {
    position: absolute; left: 0; top: 460px; width: 679px;
    text-align: center;
    font-family: "Open Sans", sans-serif; font-weight: 700;
    font-size: 39px; line-height: 43px;
    color: var(--ink);
  }
  .portrait {
    position: absolute; left: 340px; top: 555px;
    width: 339px; height: 463px;
    border-radius: 46% 54% 0 0 / 34% 38% 0 0;
    background:
      radial-gradient(circle at 58% 30%, var(--photo-glow) 0%, rgba(255,154,60,0.55) 12%, transparent 34%),
      radial-gradient(ellipse at 55% 70%, rgba(255,120,60,0.45) 0%, transparent 40%),
      linear-gradient(160deg, var(--photo-mid) 0%, var(--photo-dark) 70%);
  }
  .tagline {
    position: absolute; left: 45px; top: 609px;
    font-family: "Bebas Neue", sans-serif;
    font-size: 41px; line-height: 53px;
    color: var(--ink);
    list-style: none;
    z-index: 1;
  }
  .author-band {
    position: absolute; left: 0; top: 955px;
    width: 357px; height: 42px;
    background: linear-gradient(90deg, var(--blue-bright) 0%, var(--blue-deep) 50%, var(--blue-bright) 100%);
    z-index: 1;
  }
  .author-name {
    position: absolute; left: 45px; top: 3px;
    font-family: "Open Sans", sans-serif; font-weight: 700;
    font-size: 31px; letter-spacing: 4px; line-height: 36px;
    color: var(--white);
  }
</style>
</head>
<body>
  <main class="cover">
    <svg class="title-art" viewBox="0 0 679 560" aria-label="Steering Through the Era of Circuits">
      <defs>
        <linearGradient id="title-blue" x1="0" y1="0" x2="0" y2="1">
          <stop offset="0" stop-color="var(--blue-deep)"/>
          <stop offset="1" stop-color="var(--blue-bright)"/>
        </linearGradient>
      </defs>
      <text class="title-line" x="44" y="112" font-size="70" textLength="590" lengthAdjust="spacingAndGlyphs" fill="url(#title-blue)">STEERING THROUGH</text>
      <text class="title-line" x="44" y="193" font-size="94" textLength="590" lengthAdjust="spacingAndGlyphs" fill="var(--ink)">THE ERA OF</text>
      <text class="title-line" x="44" y="430" font-size="124" textLength="590" lengthAdjust="spacingAndGlyphs" transform="translate(0 -330) scale(1 1.75)" fill="url(#title-blue)">CIRCUITS</text>
    </svg>

    <p class="subtitle">ENDURING INSIGHT FOR<br>AN AUTOMATED CENTURY</p>

    <div class="portrait" role="img" aria-label="Profile silhouette with a glowing neural brain and light filaments in a starry blue and orange double exposure"></div>

    <ul class="tagline">
      <li>Stoic strategy,</li>
      <li>ethical clarity and</li>
      <li>human leadership</li>
      <li>in the</li>
      <li>rise of artificial</li>
      <li>intelligence</li>
    </ul>

    <div class="author-band">
      <span class="author-name">DANIEL MARSH</span>
    </div>
  </main>
</body>
</html>
```